Brantmoor Cardio

Hi 7 Dots, we need a full set of stationary to match our new logo. We need A4 and A5 letter head, business cards with compliments slips, appointment card, envelopes.
Cheers Pam

Industry/Entity Type

Business

```html
<!DOCTYPE html>
<html lang="en">
<head>
<meta charset="utf-8">
<title>Brantmoor Cardiology Clinic – Stationery</title>
<link rel="stylesheet" href="https://fonts.googleapis.com/css2?family=Arimo:wght@400;700&family=Roboto+Condensed:wght@700&display=swap">
<style>
  :root {
    --backdrop: #b3b3b3;
    --paper: #ffffff;
    --clinic-red: #730c12;
    --ink: #555555;
    --ink-dark: #4a4a4a;
    --faint: #eeeeee;
    --rule: #666666;
  }
  * { box-sizing: border-box; margin: 0; padding: 0; }
  html, body { width: 1200px; height: 1000px; overflow: hidden; }
  body { background: var(--backdrop); font-family: "Arimo", Arial, sans-serif; color: var(--ink); position: relative; }

  .card { position: absolute; width: 522px; height: 319px; box-shadow: 0 6px 10px rgba(0,0,0,0.28); overflow: hidden; }
  .card--front { background: var(--paper); }
  .card--back { background: var(--clinic-red); }
  .card--compliments { left: 69px; top: 148px; }
  .card--contact-back { left: 609px; top: 148px; }
  .card--business { left: 69px; top: 532px; }
  .card--appointment { left: 609px; top: 532px; }

  .base-band { position: absolute; left: 0; bottom: 0; width: 100%; height: 21px; background: var(--clinic-red); }

  .brand { position: absolute; display: flex; align-items: center; gap: 10px; }
  .brand__dot { width: 36px; height: 36px; border-radius: 50%; background: var(--clinic-red); flex: none; }
  .brand__name { font-weight: 700; color: var(--ink-dark); line-height: 1; }
  .brand__name span { display: block; }
  .brand__main { font-size: 25px; letter-spacing: 0.2px; }
  .brand__sub { font-size: 12px; letter-spacing: 1px; margin-top: 4px; }
  .card--front .brand { left: 23px; top: 38px; }
  .brand--reversed .brand__name { color: var(--paper); }
  .brand--reversed .brand__dot { background: var(--paper); }

  .faint-circle { position: absolute; border-radius: 50%; border: 14px solid var(--faint); width: 170px; height: 170px; }
  .card--compliments .faint-circle { left: 315px; top: 140px; }
  .card--business .faint-circle { left: 312px; top: 135px; }
  .faint-rule { position: absolute; height: 4px; background: var(--faint); }

  .doctor-name { position: absolute; left: 291px; top: 164px; font-size: 24px; color: var(--ink); }
  .credentials { position: absolute; left: 292px; top: 198px; font-family: "Roboto Condensed", "Arial Narrow", sans-serif; font-weight: 700; font-size: 11px; line-height: 19px; color: var(--ink-dark); }
  .compliments { position: absolute; left: 23px; top: 248px; font-size: 13.5px; color: var(--ink); }

  .address { font-size: 13.5px; line-height: 18.6px; color: var(--ink-dark); }
  .address strong { font-weight: 700; }
  .card--business .address { position: absolute; left: 23px; top: 216px; }

  .contact-panel { position: absolute; left: 289px; top: 10px; width: 224px; height: 299px; background: var(--paper); }
  .contact-panel .address { position: absolute; left: 18px; }
  .contact-panel .address--city { top: 40px; }
  .contact-panel .address--east { top: 166px; }
  .tick-box { position: absolute; left: 183px; width: 24px; height: 24px; border: 1.5px solid var(--rule); }
  .tick-box--city { top: 105px; }
  .tick-box--east { top: 231px; }

  .card--contact-back .brand { left: 31px; top: 133px; }
  .card--contact-back .brand__dot { width: 40px; height: 40px; }
  .card--appointment .brand { left: 67px; top: 29px; gap: 7px; }
  .card--appointment .brand__dot { width: 26px; height: 26px; }
  .card--appointment .brand__main { font-size: 17px; }
  .card--appointment .brand__sub { font-size: 8.5px; margin-top: 2px; }

  .appointment-title { position: absolute; left: 10px; width: 269px; top: 94px; text-align: center; color: var(--paper); font-size: 17px; letter-spacing: 0.3px; }
  .appointment-table { position: absolute; left: 10px; top: 136px; width: 269px; height: 173px; background: var(--paper); }
  .appointment-table__head { position: absolute; top: 9px; font-size: 15px; color: var(--ink); }
  .appointment-table__head--date { left: 59px; }
  .appointment-table__head--time { left: 197px; }
  .appointment-table__line { position: absolute; height: 1.5px; background: var(--rule); }
  .line--date { left: 5px; width: 151px; }
  .line--time { left: 168px; width: 96px; }
</style>
</head>
<body>

  <section class="card card--front card--compliments">
    <div class="brand">
      <div class="brand__dot"></div>
      <div class="brand__name"><span class="brand__main">BRANTMOOR</span><span class="brand__sub">CARDIOLOGY CLINIC</span></div>
    </div>
    <div class="faint-circle"></div>
    <div class="faint-rule" style="left:150px; top:254px; width:372px;"></div>
    <p class="doctor-name">Dr Rahim Kassar</p>
    <p class="credentials">M.B.B.S - MBMBBS (Pak) - FCPS-Medicine (Pak)<br>FCPS-Cardiology (Pak) - FRACP (Australia)</p>
    <p class="compliments">With Compliments</p>
    <div class="base-band"></div>
  </section>

  <section class="card card--back card--contact-back">
    <div class="brand brand--reversed">
      <div class="brand__dot"></div>
      <div class="brand__name"><span class="brand__main">BRANTMOOR</span><span class="brand__sub">CARDIOLOGY CLINIC</span></div>
    </div>
    <div class="contact-panel">
      <p class="address address--city"><strong>Brantmoor Cardiology Clinic</strong><br>148 Alder Street<br>HARTWELL SA 5010<br>Phone (08) 81460372<br>Fax (08) 81460389</p>
      <p class="address address--east"><strong>Brantmoor Cardiology Clinic</strong><br>Shop 4, 22-24 Linden Avenue<br>MARLOW EAST SA 5120<br>Phone (08) 85907214<br>Fax (08) 85907219</p>
    </div>
  </section>

  <section class="card card--front card--business">
    <div class="brand">
      <div class="brand__dot"></div>
      <div class="brand__name"><span class="brand__main">BRANTMOOR</span><span class="brand__sub">CARDIOLOGY CLINIC</span></div>
    </div>
    <div class="faint-circle"></div>
    <div class="faint-rule" style="left:174px; top:255px; width:348px;"></div>
    <p class="address">148 Alder Street<br>HARTWELL SA 5010<br>Phone (08) 81460372<br>Fax (08) 81460389</p>
    <div class="base-band"></div>
  </section>

  <section class="card card--back card--appointment">
    <div class="brand brand--reversed">
      <div class="brand__dot"></div>
      <div class="brand__name"><span class="brand__main">BRANTMOOR</span><span class="brand__sub">CARDIOLOGY CLINIC</span></div>
    </div>
    <p class="appointment-title">YOUR NEXT APPOINTMENT</p>
    <div class="appointment-table">
      <span class="appointment-table__head appointment-table__head--date">DATE</span>
      <span class="appointment-table__head appointment-table__head--time">TIME</span>
      <div class="appointment-table__line line--date" style="top:61px;"></div>
      <div class="appointment-table__line line--time" style="top:61px;"></div>
      <div class="appointment-table__line line--date" style="top:98px;"></div>
      <div class="appointment-table__line line--time" style="top:98px;"></div>
      <div class="appointment-table__line line--date" style="top:135px;"></div>
      <div class="appointment-table__line line--time" style="top:135px;"></div>
    </div>
    <div class="contact-panel">
      <p class="address address--city"><strong>Brantmoor Cardiology Clinic</strong><br>148 Alder Street<br>HARTWELL SA 5010<br>Phone (08) 81460372<br>Fax (08) 81460389</p>
      <div class="tick-box tick-box--city"></div>
      <p class="address address--east"><strong>Brantmoor Cardiology Clinic</strong><br>Shop 4, 22-24 Linden Avenue<br>MARLOW EAST SA 5120<br>Phone (08) 85907214<br>Fax (08) 85907219</p>
      <div class="tick-box tick-box--east"></div>
    </div>
  </section>

</body>
</html>
```